Brightway Dwelling & Yard Care - Maintenance & Improvements

Handyman service - Total home improvement and maintenance

We do everything indoors, ie. carpentry, and outdoors, ie. garden maintenance

No job too small or too unusual

7 Days per week
Updates

I want the overall impression not to favour either gender ... eg. maybe don't use the word Handy'man' because we also have a Fixmistress service .... but just stay with a generic theme of home improvement and maintenance

Industry/Entity Type

Home Improvement

Contact Information for Business Card

Brightway Dwelling & Yard Care
7 Days per Week
Total Home Maintenance and Improvements
Handyman | Fixmistress | Our (DIY) Task Pal
Ph: 0487 613 902
www.brightwaydwellingyard.com.au

Requirements
Must have
• The black and white image of various workers, as per attached

```html
<!DOCTYPE html>
<html lang="en">
<head>
<meta charset="utf-8">
<title>Brightway Dwelling &amp; Yard Care – Business Card</title>
<link rel="stylesheet" href="https://fonts.googleapis.com/css2?family=Almendra&family=Arimo:wght@400&display=swap">
<style>
  :root {
    --paper: #ffffff;
    --ink: #111111;
    --rule-dark: #1a1a1a;
    --rule-light: rgba(26, 26, 26, 0);
    --strip-dark: #1c1c1c;
    --strip-mid: #5a5a5a;
  }
  html, body {
    margin: 0;
    padding: 0;
    overflow: hidden;
    background: var(--paper);
  }
  .card {
    position: relative;
    width: 1200px;
    height: 741px;
    background: var(--paper);
    color: var(--ink);
    overflow: hidden;
  }
  .brand-name {
    position: absolute;
    top: 50px;
    left: 0;
    width: 100%;
    margin: 0;
    text-align: center;
    font-family: "Almendra", serif;
    font-weight: 400;
    font-size: 66px;
    line-height: 1;
    letter-spacing: 0.5px;
  }
  .tagline {
    position: absolute;
    top: 160px;
    left: 0;
    width: 100%;
    margin: 0;
    text-align: center;
    font-family: "Arimo", sans-serif;
    font-size: 29px;
    line-height: 38px;
  }
  .divider {
    position: absolute;
    top: 305px;
    left: 142px;
    width: 916px;
    height: 4px;
    background: linear-gradient(to right, var(--rule-light), var(--rule-dark) 50%, var(--rule-light));
  }
  .contact {
    position: absolute;
    top: 362px;
    left: 0;
    width: 100%;
    margin: 0;
    text-align: center;
    font-family: "Arimo", sans-serif;
    font-size: 40px;
    line-height: 51px;
    font-style: normal;
  }
  .trades-strip {
    position: absolute;
    left: 60px;
    top: 584px;
    width: 1097px;
    height: 114px;
    background: linear-gradient(to right, var(--strip-dark), var(--strip-mid) 50%, var(--strip-dark));
  }
</style>
</head>
<body>
  <main class="card">
    <h1 class="brand-name">Brightway Dwelling &amp; Yard Care</h1>
    <p class="tagline">
      Total Home Maintenance and Improvements<br>
      Handyman | Fixmistress | Our (DIY) Task Pal
    </p>
    <div class="divider"></div>
    <address class="contact">
      7 Days per Week<br>
      Ph: 0487 613 902<br>
      www.brightwaydwellingyard.com.au
    </address>
    <div class="trades-strip" role="img" aria-label="Row of black silhouette figures doing home and garden jobs: carpentry, wheelbarrow, painting, ladder work, spraying, hedge trimming, mowing, plumbing, flower beds, watering and digging"></div>
  </main>
</body>
</html>
```